Website for new child psychology practice

New clinical psychology practice in NSW Australia, specialising in work with children, adolescents and families. I would like to feature the colours in the logo, which was recently designed by pixelmesa designer Odette.
I am seeking a professional looking page, which is easy to navigate and is colourful and playful but not childish.
Target Market(s)
Parents and professionals
Industry/Entity Type
Health
Coding
Coded - Design and coding required
Number of Pages Required
1 page
Font styles to use
Serif
Requirements
Must have
- Pages for 'About us' 'Services' 'Fees and information' 'Contact us'
Should not have
- Childish stock photos

```html
<!DOCTYPE html>
<html lang="en">
<head>
<meta charset="utf-8">
<title>Dr Clara Wren — Clinical Psychologist</title>
<link rel="stylesheet" href="https://fonts.googleapis.com/css2?family=Libre+Baskerville:wght@400;700&family=Open+Sans:wght@400;600;700&display=swap">
<style>
:root{
  --purple:#a3258e;
  --purple-soft:#b64aa3;
  --orange:#e0601c;
  --ink:#2f2f33;
  --muted:#6b6b70;
  --line:#e6e1e8;
  --white:#ffffff;
  --page:#ffffff;
}
*{box-sizing:border-box;margin:0;padding:0}
html,body{width:1200px;height:4841px;overflow:hidden}
body{position:relative;background:var(--page);font-family:"Open Sans",Arial,sans-serif;color:var(--ink)}
.abs{position:absolute}
.serif{font-family:"Libre Baskerville",Georgia,serif;font-weight:700}
.photo{position:absolute}
.eyebrow{font-size:11px;letter-spacing:.3px;color:var(--orange);text-transform:uppercase;display:flex;align-items:center;gap:12px}
.eyebrow::after{content:"";width:48px;height:2px;background:var(--orange)}
.eyebrow.center::before{content:"";width:48px;height:2px;background:var(--orange)}
.btn-orange{position:absolute;background:var(--orange);color:#fff;font-weight:700;font-size:13px;border-radius:6px;display:flex;align-items:center;justify-content:center}
p.body{font-size:12.5px;line-height:24px;color:var(--muted)}

/* header */
.topbar{position:absolute;left:0;top:0;width:1200px;height:85px;background:#fff;border-bottom:1px solid var(--line)}
.topbar .greeting{position:absolute;left:395px;top:11px;font-size:13px;color:var(--ink)}
.topbar .mail{position:absolute;left:626px;top:6px;font-size:13px;display:flex;align-items:center;gap:8px}
.mail-dot{width:26px;height:26px;border-radius:50%;background:var(--purple);display:flex;align-items:center;justify-content:center}
.nav{position:absolute;top:54px;left:338px;font-size:12.5px}
.nav a{position:absolute;white-space:nowrap;color:var(--ink);text-decoration:none}
.logo-oval{position:absolute;left:138px;top:-4px;width:168px;height:100px;border-radius:50%;background:#fff;box-shadow:0 4px 10px rgba(0,0,0,.08);display:flex;align-items:center;justify-content:center;gap:6px;z-index:3}
.logo-oval span{font-family:"Libre Baskerville",Georgia,serif;font-weight:700;color:var(--purple);font-size:14px}
.call{position:absolute;left:855px;top:0;width:203px;height:86px;background:var(--purple);color:#fff;z-index:3}
.call small{position:absolute;left:48px;top:18px;font-size:13px}
.call strong{position:absolute;left:48px;top:42px;font-size:20px}
.call .ring{position:absolute;left:-8px;top:24px;width:38px;height:38px;border-radius:50%;background:#fff;border:2px solid var(--orange);display:flex;align-items:center;justify-content:center}

/* hero */
.hero-card{position:absolute;left:75px;top:270px;width:605px;height:363px;background:#fff}
.hero-card::before{content:"";position:absolute;left:0;top:58px;width:8px;height:110px;background:var(--orange)}
.hero-card h1{position:absolute;left:48px;top:48px;font-size:56px;line-height:70px;color:var(--purple)}
.hero-card p{position:absolute;left:48px;top:196px;width:440px;font-size:11.5px;line-height:21px;color:var(--muted)}

/* features */
.features{position:absolute;left:90px;top:1531px;width:1016px;height:214px;background:#fff;border-radius:0 0 90px 90px;box-shadow:0 6px 22px rgba(0,0,0,.09)}
.feature{position:absolute;top:36px;width:260px}
.feature .ic{position:absolute;left:0;top:0;width:62px;height:62px;border-radius:50%;border:2px solid #2e5a87;display:flex;align-items:center;justify-content:center}
.feature h3{position:absolute;left:80px;top:10px;font-size:20px;color:var(--purple)}
.feature .more{position:absolute;left:82px;top:44px;font-size:14px;color:var(--orange)}
.feature p{position:absolute;left:80px;top:74px;width:185px;font-size:12px;line-height:22px;color:var(--ink)}

/* services */
.svc-arrow{position:absolute;top:1870px;width:42px;height:60px;border-radius:6px;background:#fff;box-shadow:0 2px 10px rgba(0,0,0,.14);display:flex;align-items:center;justify-content:center}
.svc-box{position:absolute;top:2150px;width:273px;height:199px;background:#fff;box-shadow:0 4px 14px rgba(0,0,0,.09);padding:28px 30px 28px 38px}
.svc-box h3{font-size:16.5px;color:var(--purple);margin-bottom:16px;white-space:nowrap}
.svc-box p{font-size:12px;line-height:24px;color:var(--ink)}
.svc-box .read{display:block;margin-top:14px;font-weight:700;font-size:14px;color:var(--orange)}
.svc-box.active{background:var(--purple)}
.svc-box.active h3,.svc-box.active p,.svc-box.active .read{color:#fff}
.btn-outline{position:absolute;left:513px;top:2393px;width:167px;height:45px;border:2px solid var(--purple);border-radius:6px;display:flex;align-items:center;justify-content:center;font-weight:700;font-size:13px;color:var(--purple)}

.section-title{position:absolute;left:0;width:1200px;text-align:center;color:var(--purple);font-size:40px}

/* gallery */
.g-arrow{position:absolute;top:2875px;width:66px;height:94px;background:#fff;border-radius:4px;display:flex;align-items:center;justify-content:center;box-shadow:0 2px 10px rgba(0,0,0,.12)}
.caption{position:absolute;left:259px;top:2999px;width:597px;height:79px;background:#fff;display:flex;align-items:center;padding-left:38px;font-weight:700;font-size:22px;color:var(--ink)}
.caption-go{position:absolute;left:856px;top:2999px;width:79px;height:79px;background:var(--orange);display:flex;align-items:center;justify-content:center}

/* reviews */
.review{position:absolute;top:3392px;width:323px;height:263px;background:#fff;box-shadow:0 3px 14px rgba(0,0,0,.1);text-align:center}
.review .avatar{position:absolute;left:129px;top:-34px;width:64px;height:64px;border-radius:50%;background:linear-gradient(160deg,#c9d6e6,#7c94b3)}
.review .stars{position:absolute;left:0;top:62px;width:100%;color:var(--orange);font-size:18px;letter-spacing:8px}
.review p{position:absolute;left:44px;top:102px;width:235px;font-size:12.5px;line-height:24px;color:var(--muted)}
.review .quote{position:absolute;left:127px;top:225px;width:68px;height:38px;border-radius:34px 34px 0 0;background:var(--purple);display:flex;justify-content:center;padding-top:8px}
.reviewer{position:absolute;top:3686px;width:323px;text-align:center}
.reviewer b{display:block;font-size:17px;color:var(--ink)}
.reviewer span{display:block;font-size:12px;color:var(--muted);margin-top:6px}

/* contact */
.contact-card{position:absolute;left:648px;top:3978px;width:466px;height:477px;background:var(--purple);border-radius:22px;box-shadow:0 0 0 5px #fff,0 0 0 7px #e8d6e5;color:#fff;text-align:center}
.contact-card h2{position:absolute;left:0;top:44px;width:100%;font-size:27px;font-weight:600}
.contact-card p{position:absolute;left:60px;top:90px;width:346px;font-size:12px;line-height:18px}
.field{position:absolute;left:37px;width:393px;height:45px;border-radius:4px;background:var(--purple-soft);text-align:left;padding:16px 28px;font-size:10px;letter-spacing:.3px}
.submit{position:absolute;left:37px;top:388px;width:393px;height:45px;border-radius:4px;background:#fff;color:var(--purple);font-weight:700;font-size:15px;display:flex;align-items:center;justify-content:center}

/* footer */
.f-head{position:absolute;top:4553px;font-size:14px;color:var(--purple)}
.f-head::after{content:"";display:block;margin-top:14px;width:120px;height:1px;background:var(--line)}
.f-link{position:absolute;font-size:14px;color:var(--ink)}
.f-item{position:absolute;font-size:14px;color:var(--ink);display:flex;align-items:flex-start;gap:18px;line-height:22px}
.social{width:28px;height:28px;border-radius:50%;background:#eee}
</style>
</head>
<body>

<div class="photo" role="img" aria-label="Photo of a client lying on a couch talking with a therapist" style="left:0;top:85px;width:1200px;height:780px;background:linear-gradient(110deg,#6e6257 0%,#a79a8c 35%,#d8d2cb 60%,#8e8680 100%)"></div>
<svg class="abs" style="left:0;top:700px" width="1200" height="170" viewBox="0 0 1200 170" aria-hidden="true">
  <path d="M0 90 C180 150 420 170 640 120 C860 70 1050 40 1200 130 L1200 170 L0 170Z" fill="#fff"/>
  <path d="M0 90 C180 140 420 150 640 100 C860 50 1040 40 1200 110 L1200 130 C1050 60 860 80 640 120 C420 170 180 150 0 110Z" fill="var(--purple)"/>
  <path d="M0 70 C150 140 380 145 600 110 C760 85 900 70 1000 95 C880 75 760 95 600 125 C380 165 150 150 0 100Z" fill="var(--orange)"/>
</svg>

<header class="topbar">
  <div class="greeting">WELCOME</div>
  <div class="mail"><span class="mail-dot"><svg width="14" height="10" viewBox="0 0 14 10"><rect x=".5" y=".5" width="13" height="9" rx="1" fill="none" stroke="#fff"/><path d="M1 1l6 5 6-5" fill="none" stroke="#fff"/></svg></span>hello@wrenpractice.com</div>
  <nav class="nav">
    <a style="left:0;color:#2e5a87;font-weight:700">HOME</a>
    <a style="left:67px">About Us</a>
    <a style="left:163px">Services</a>
    <a style="left:254px">Fees &amp; Info</a>
    <a style="left:347px">Gallery</a>
    <a style="left:436px">Contact Us</a>
  </nav>
</header>
<div class="logo-oval"><i style="width:16px;height:16px;border-radius:50%;background:var(--orange)"></i><span>Dr Clara Wren</span></div>
<div class="call">
  <span class="ring"><svg width="18" height="18" viewBox="0 0 24 24"><path d="M6.6 10.8a15 15 0 0 0 6.6 6.6l2.2-2.2a1 1 0 0 1 1-.25 11.4 11.4 0 0 0 3.6.57 1 1 0 0 1 1 1V20a1 1 0 0 1-1 1A17 17 0 0 1 3 4a1 1 0 0 1 1-1h3.5a1 1 0 0 1 1 1c0 1.25.2 2.450.57 3.57a1 1 0 0 1-.25 1z" fill="var(--orange)"/></svg></span>
  <small>Call us today at</small><strong>(02) 555-0148</strong>
</div>

<div class="hero-card">
  <h1 class="serif">Your Path to<br>Fulfillment</h1>
  <p>Lorem ipsum dolor sit amet, consectetur adipiscing elit, sed do eiusmod tempor incididunt ut labore et dolore magna aliqua. Ut enim</p>
  <div class="btn-orange" style="left:49px;top:271px;width:167px;height:47px">Learn More</div>
</div>

<div class="photo" role="img" aria-label="Photo of a smiling therapist in a session" style="left:103px;top:971px;width:300px;height:316px;border-radius:110px 0 0 0;background:linear-gradient(150deg,#8a7263,#c9b7a6 60%,#e9e2da)"></div>
<div class="photo" role="img" aria-label="Photo of a group counselling session" style="left:430px;top:993px;width:118px;height:120px;border-radius:28px 0 0 0;background:linear-gradient(150deg,#9a8c86,#d4cbc4)"></div>
<div class="photo" role="img" aria-label="Photo of a psychologist taking notes with a client" style="left:268px;top:1132px;width:303px;height:314px;border-radius:90px 0 110px 0;background:linear-gradient(140deg,#d9d2cb,#8b7a70 55%,#3d3a3c)"></div>
<div class="abs" style="left:240px;top:1216px;width:98px;height:98px;border-radius:50%;background:#fff;display:flex;align-items:center;justify-content:center"><i style="width:26px;height:26px;border-radius:50%;background:var(--purple)"></i></div>

<div class="eyebrow abs" style="left:625px;top:990px">About Us</div>
<h2 class="serif abs" style="left:622px;top:1030px;font-size:36px;line-height:56px;color:var(--purple)">Inspiring Confidence,<br>Igniting Change</h2>
<p class="body abs" style="left:625px;top:1155px;width:440px">Lorem ipsum dolor sit amet, consectetur adipiscing elit, sed do eiusmod tempor incididunt ut labore et dolore magna aliqua. Ut enim ad min im veniam, quis nostrud exercitation ullamco laboris nisi ut aliquip ex ea commodo consequat. Duis aute irure dolor in reprehenderit in voluptate velit esse cillum dolore eu fugiat nulla pariatur. Excepteur sint occaecat cupidatat non proident, sunt in culpa qui officia deserunt mollit anim id est laborum.</p>
<div class="btn-orange" style="left:625px;top:1346px;width:168px;height:46px">Learn More</div>

<section class="features">
  <div class="feature" style="left:58px">
    <span class="ic"><svg width="26" height="26" viewBox="0 0 26 26"><g stroke="var(--purple)" stroke-width="2" stroke-linecap="round"><path d="M13 3v4M13 19v4M3 13h4M19 13h4M6 6l3 3M17 17l3 3M20 6l-3 3M9 17l-3 3"/></g></svg></span>
    <h3 class="serif">Expertise</h3><span class="more">Learn More</span>
    <p>Lorem ipsum dolor sit amet, consectetur adipiscing elit, se do eiusmod tempor e</p>
  </div>
  <div class="feature" style="left:366px">
    <span class="ic"><svg width="26" height="26" viewBox="0 0 26 26"><g fill="var(--purple)"><path d="M13 4l1.5 4.5L19 10l-4.5 1.5L13 16l-1.5-4.5L7 10l4.5-1.5z"/><circle cx="6" cy="19" r="2"/><circle cx="20" cy="19" r="2"/><circle cx="13" cy="22" r="1.6"/></g></svg></span>
    <h3 class="serif">Experience</h3><span class="more">Learn More</span>
    <p>Lorem ipsum dolor sit amet, consectetur adipiscing elit, se do eiusmod tempor e</p>
  </div>
  <div class="feature" style="left:676px">
    <span class="ic"><svg width="26" height="26" viewBox="0 0 26 26"><g fill="none" stroke="var(--purple)" stroke-width="2"><path d="M5 14a8 8 0 0 1 16 0"/><rect x="3" y="13" width="5" height="7" rx="2"/><rect x="18" y="13" width="5" height="7" rx="2"/></g></svg></span>
    <h3 class="serif">Professionalism</h3><span class="more">Learn More</span>
    <p>Lorem ipsum dolor sit amet, consectetur adipiscing elit, se do eiusmod tempor e</p>
  </div>
</section>

<div class="eyebrow abs" style="left:98px;top:1851px">Services</div>
<h2 class="serif abs" style="left:95px;top:1890px;font-size:40px;color:var(--purple)">Our Services</h2>
<div class="svc-arrow" style="left:1007px"><svg width="12" height="16" viewBox="0 0 12 16"><path d="M9 2L3 8l6 6" fill="none" stroke="#222" stroke-width="2.5"/></svg></div>
<div class="svc-arrow" style="left:1059px"><svg width="12" height="16" viewBox="0 0 12 16"><path d="M3 2l6 6-6 6" fill="none" stroke="#222" stroke-width="2.5"/></svg></div>

<div class="photo" role="img" aria-label="Photo of a family therapy session" style="left:90px;top:1974px;width:323px;height:233px;background:linear-gradient(135deg,#b89b82,#e6dfd8 55%,#9c8f88)"></div>
<div class="photo" role="img" aria-label="Photo of a client talking with a counsellor" style="left:436px;top:1974px;width:323px;height:233px;background:linear-gradient(135deg,#cfc7bd,#7f7a72 55%,#d8d2c8)"></div>
<div class="photo" role="img" aria-label="Photo of a therapist writing on a clipboard" style="left:787px;top:1974px;width:321px;height:233px;background:linear-gradient(135deg,#e3ddd6,#a39a93 50%,#c76c36)"></div>

<div class="svc-box" style="left:120px"><h3 class="serif">Family Therapy</h3><p>Lorem ipsum dolor sit amet, consectetur adipiscing elit, sed do eiusmod tempor incididunt ut nn</p><span class="read">Read More</span></div>
<div class="svc-box active" style="left:456px;width:282px"><h3 class="serif">Behavioral Intervention</h3><p>Lorem ipsum dolor sit amet, consectetur adipiscing elit, sed do eiusmod tempor incididunt ut nn</p><span class="read">Read More</span></div>
<div class="svc-box" style="left:806px;width:283px"><h3 class="serif">Habit Formation</h3><p>Lorem ipsum dolor sit amet, consectetur adipiscing elit, sed do eiusmod tempor incididunt ut nn</p><span class="read">Read More</span></div>
<div class="btn-outline">Learn More</div>

<div class="abs" style="left:0;top:2524px;width:1200px;height:1px;background:var(--line)"></div>

<div class="eyebrow center abs" style="left:0;width:1200px;justify-content:center;top:2584px">Our Gallery</div>
<h2 class="serif section-title" style="top:2614px">Our Recent Videos</h2>
<div class="photo" role="img" aria-label="Video thumbnail of an office meeting" style="left:0;top:2716px;width:180px;height:400px;border-radius:0 0 90px 0;background:linear-gradient(135deg,#4f4a46,#9b8e83)"></div>
<div class="photo" role="img" aria-label="Video thumbnail of a counselling conversation" style="left:220px;top:2716px;width:757px;height:400px;border-radius:70px 0 90px 0;background:linear-gradient(120deg,#8b6a55,#d9cfc4 45%,#b7ab9e 75%,#7c6a5e)"></div>
<div class="photo" role="img" aria-label="Video thumbnail of colleagues working at a desk" style="left:1014px;top:2716px;width:186px;height:400px;border-radius:70px 0 0 0;background:linear-gradient(135deg,#3d3b3a,#8d8278)"></div>
<div class="g-arrow" style="left:92px"><svg width="14" height="22" viewBox="0 0 14 22"><path d="M11 2L3 11l8 9" fill="none" stroke="var(--orange)" stroke-width="3"/></svg></div>
<div class="g-arrow" style="left:1039px"><svg width="14" height="22" viewBox="0 0 14 22"><path d="M3 2l8 9-8 9" fill="none" stroke="var(--orange)" stroke-width="3"/></svg></div>
<div class="caption">Overcoming Status Anxiety</div>
<div class="caption-go"><svg width="28" height="22" viewBox="0 0 28 22"><path d="M2 11h22M16 3l8 8-8 8" fill="none" stroke="#fff" stroke-width="2.5"/></svg></div>

<div class="eyebrow center abs" style="left:0;width:1200px;justify-content:center;top:3221px">Testimonials</div>
<h2 class="serif section-title" style="top:3250px">Client Reviews</h2>

<div class="review" style="left:90px"><span class="avatar" role="img" aria-label="Client portrait"></span><div class="stars">★★★★★</div><p>Lorem ipsum dolor sit amet, consectetur adipiscing elit, sed do eiusmod tempor incididunt ut labore et dolore</p><span class="quote"><svg width="24" height="18" viewBox="0 0 24 18"><path d="M2 18V10C2 5 5 2 9 1v4C7 6 6 8 6 10h4v8zM14 18V10c0-5 3-8 7-9v4c-2 1-3 3-3 5h4v8z" fill="#fff"/></svg></span></div>
<div class="review" style="left:441px"><span class="avatar" role="img" aria-label="Client portrait"></span><div class="stars">★★★★★</div><p>Lorem ipsum dolor sit amet, consectetur adipiscing elit, sed do eiusmod tempor incididunt ut labore et dolore</p><span class="quote"><svg width="24" height="18" viewBox="0 0 24 18"><path d="M2 18V10C2 5 5 2 9 1v4C7 6 6 8 6 10h4v8zM14 18V10c0-5 3-8 7-9v4c-2 1-3 3-3 5h4v8z" fill="#fff"/></svg></span></div>
<div class="review" style="left:791px"><span class="avatar" role="img" aria-label="Client portrait"></span><div class="stars">★★★★★</div><p>Lorem ipsum dolor sit amet, consectetur adipiscing elit, sed do eiusmod tempor incididunt ut labore et dolore</p><span class="quote"><svg width="24" height="18" viewBox="0 0 24 18"><path d="M2 18V10C2 5 5 2 9 1v4C7 6 6 8 6 10h4v8zM14 18V10c0-5 3-8 7-9v4c-2 1-3 3-3 5h4v8z" fill="#fff"/></svg></span></div>
<div class="reviewer" style="left:90px"><b>Tom Hallett</b><span>Country</span></div>
<div class="reviewer" style="left:441px"><b>Tom Hallett</b><span>Country</span></div>
<div class="reviewer" style="left:791px"><b>Tom Hallett</b><span>Country</span></div>

<div class="photo" role="img" aria-label="Photo of a woman reading a tablet in a bright office" style="left:0;top:3897px;width:1200px;height:501px;background:linear-gradient(100deg,#cfc9c1,#ece8e2 40%,#bdb4aa 70%,#8e8882)"></div>
<div class="photo" role="img" aria-label="Woman holding a tablet, standing" style="left:180px;top:3765px;width:440px;height:633px;border-radius:160px 160px 0 0;background:linear-gradient(180deg,#5a3d2c 0%,#efeae3 25%,#e8e1d8 60%,#a98a62 100%)"></div>
<form class="contact-card">
  <h2>Get in touch with us</h2>
  <p>Lorem ipsum dolor sit amet, consectetur adipiscing elit, sed do eiusmod tempor incididunt ut</p>
  <div class="field" style="top:139px">NAAM</div>
  <div class="field" style="top:214px">EMAIL</div>
  <div class="field" style="top:289px">BERICHT</div>
  <div class="submit">SUBMIT</div>
</form>

<div class="abs" style="left:98px;top:4578px;display:flex;align-items:center;gap:8px"><i style="width:28px;height:28px;border-radius:50%;background:var(--purple)"></i><span class="serif" style="font-size:19px;color:var(--purple)">Dr Clara Wren</span></div>
<div class="abs" style="left:112px;top:4670px;display:flex;align-items:center;gap:12px;font-size:14px;color:var(--purple)">Follow Us <i class="social"></i><i class="social"></i><i class="social"></i></div>

<div class="f-head" style="left:364px">Quick Links</div>
<div class="f-link" style="left:364px;top:4603px">Home</div>
<div class="f-link" style="left:364px;top:4635px">About Us</div>
<div class="f-link" style="left:364px;top:4667px">Services</div>
<div class="f-link" style="left:364px;top:4699px">Contact us</div>

<div class="f-head" style="left:586px">Contact us</div>
<div class="f-item" style="left:600px;top:4603px"><svg width="14" height="18" viewBox="0 0 14 18"><path d="M7 0a7 7 0 0 1 7 7c0 5-7 11-7 11S0 12 0 7a7 7 0 0 1 7-7z" fill="var(--orange)"/><circle cx="7" cy="7" r="2.5" fill="#fff"/></svg><span>1234 Location<br>1456 Street</span></div>
<div class="f-item" style="left:600px;top:4660px"><svg width="16" height="16" viewBox="0 0 24 24"><path d="M6.6 10.8a15 15 0 0 0 6.6 6.6l2.2-2.2a1 1 0 0 1 1-.25 11.4 11.4 0 0 0 3.6.57 1 1 0 0 1 1 1V20a1 1 0 0 1-1 1A17 17 0 0 1 3 4a1 1 0 0 1 1-1h3.5a1 1 0 0 1 1 1c0 1.25.2 2.45.57 3.57a1 1 0 0 1-.25 1z" fill="var(--orange)"/></svg><span>1-800-555-0199</span></div>
<div class="f-item" style="left:600px;top:4697px"><svg width="16" height="12" viewBox="0 0 16 12"><rect width="16" height="12" rx="1" fill="var(--orange)"/><path d="M1 1l7 6 7-6" fill="none" stroke="#fff" stroke-width="1.4"/></svg><span>hello@wrenpractice.com</span></div>

<div class="f-head" style="left:860px">Subscribe to Newsletter</div>
<div class="f-link" style="left:860px;top:4603px;width:230px;font-size:13px;line-height:20px">Sign up for our newsletter to know the latest from us</div>
<div class="abs" style="left:860px;top:4657px;width:145px;height:34px;border:1px solid var(--line);font-size:11px;color:var(--muted);padding:9px 16px">Email</div>
<div class="abs" style="left:1005px;top:4657px;width:101px;height:34px;background:var(--orange);color:#fff;font-weight:700;font-size:12px;display:flex;align-items:center;justify-content:center">VERSTUUR</div>

<div class="abs" style="left:112px;top:4755px;width:976px;height:1px;background:var(--line)"></div>
<div class="abs" style="left:0;top:4794px;width:1200px;text-align:center;font-size:13px;color:var(--purple)">Dr Clara Wren</div>

</body>
</html>
```